Dance Card to Provide Contact Info

I'm looking for a double sided business card to provide contact information to perspective dance partners.
One side of the card would have the words: "Yes I would love to Dance" written in an interesting and eye catching way. Below that would be the three categories I'm interested in
>Social >Exhibition >Competition
The other side of the card would include a picture of me with my Name, Phone Number, and Email Address (Dale Pruitt, 210-574-1328, dale@twirlnstep.dance)
My target market is middle aged women interested in Country and Western dancing and West Coast Swing dancing. I am NOT particularly interested in Ballroom style.
Here are a few links to the type of dancing I want to do:
http://www.plvkrn.org/
http://www.prairiefolkstepsociety.com/
http://mesquitevalleytwostep.com/
Dale Pruitt
210-574-1328
dale@twirlnstep.dance

```html
<!DOCTYPE html>
<html lang="en">
<head>
<meta charset="utf-8">
<title>Twirl N Step Dance – Business Card</title>
<link rel="stylesheet" href="https://fonts.googleapis.com/css2?family=Roboto:wght@400;700&display=swap">
<style>
  :root {
    --page: #e8e3da;
    --card-white: #ffffff;
    --card-grey: #e9e9e9;
    --brand-red: #b3302b;
    --red-light: #c9473c;
    --red-dark: #8a201d;
    --ink: #1d1d1d;
    --rule: #2a2a2a;
    --band: #ededed;
    --white: #ffffff;
  }
  * { box-sizing: border-box; margin: 0; padding: 0; }
  html, body {
    width: 1200px; height: 1023px; overflow: hidden;
    background: var(--page);
    font-family: "Roboto", Arial, sans-serif;
  }
  .card {
    position: absolute; left: 200px; width: 800px; height: 457px;
    border-radius: 18px; overflow: hidden;
    box-shadow: 0 6px 18px rgba(0,0,0,.18);
  }

  /* ---------- Shared brand name ---------- */
  .brand { position: absolute; display: flex; align-items: center; gap: 18px; }
  .brand-dot { border-radius: 50%; background: var(--ink); flex: none; }
  .brand-name {
    font-weight: 700; text-transform: uppercase; line-height: 1.05;
  }
  .brand-name span { display: block; }
  .brand-name .brand-line-top { letter-spacing: 4px; }
  .brand-name .brand-line-bottom { letter-spacing: 14px; }

  /* ---------- Front: contact side ---------- */
  .card-front {
    top: 40px;
    background: linear-gradient(160deg, var(--card-white) 0%, var(--card-grey) 100%);
  }
  .portrait {
    position: absolute; left: 0; bottom: 0; width: 380px; height: 300px;
    background: linear-gradient(180deg, #d9a27f 0%, #c98e6c 40%, #2a2a2a 62%, #1b1b1b 100%);
    border-top-right-radius: 140px;
  }
  .card-front .brand { left: 150px; top: 36px; }
  .card-front .brand-dot { width: 62px; height: 62px; }
  .card-front .brand-name { color: var(--brand-red); font-size: 44px; }

  .contact-name {
    position: absolute; right: 92px; top: 204px;
    color: var(--brand-red); font-size: 38px; font-weight: 400; letter-spacing: .5px;
  }
  .contact-rule {
    position: absolute; left: 380px; top: 258px; width: 350px; height: 1px; background: var(--rule);
  }
  .contact-tab {
    position: absolute; left: 730px; top: 252px; width: 70px; height: 12px; background: var(--brand-red);
  }
  .contact-list { position: absolute; right: 24px; top: 276px; list-style: none; }
  .contact-list li {
    display: flex; align-items: center; justify-content: flex-end; gap: 14px;
    height: 30px; color: var(--brand-red); font-size: 17px;
  }
  .contact-icon { width: 20px; height: 20px; flex: none; }

  /* ---------- Back: tagline side ---------- */
  .card-back {
    top: 526px;
    background: radial-gradient(ellipse at 62% 40%, var(--red-light) 0%, #a9312b 55%, var(--red-dark) 100%);
  }
  .card-back .brand { left: 300px; top: 70px; }
  .card-back .brand-dot { width: 70px; height: 70px; }
  .card-back .brand-name { color: var(--white); font-size: 50px; }
  .tagline-band {
    position: absolute; left: 0; top: 290px; width: 100%; height: 64px;
    background: linear-gradient(180deg, var(--white) 0%, var(--band) 100%);
    display: flex; align-items: center; justify-content: center;
  }
  .tagline { color: var(--brand-red); font-size: 27px; letter-spacing: 1px; }
  .categories {
    position: absolute; left: 0; top: 380px; width: 100%; text-align: center;
    color: var(--white); font-size: 24px; letter-spacing: 1.5px;
  }
</style>
</head>
<body>

<section class="card card-front" aria-label="Contact side">
  <div class="portrait" role="img" aria-label="Portrait photo of Dale Pruitt in a black shirt"></div>

  <div class="brand">
    <div class="brand-dot"></div>
    <div class="brand-name"><span class="brand-line-top">Twirl N Step</span><span class="brand-line-bottom">Dance</span></div>
  </div>

  <h1 class="contact-name">Dale Pruitt</h1>
  <div class="contact-rule"></div>
  <div class="contact-tab"></div>

  <ul class="contact-list">
    <li>210-574-1328
      <svg class="contact-icon" viewBox="0 0 20 20"><circle cx="10" cy="10" r="9" fill="none" stroke="#1d1d1d" stroke-width="1.5"/><path d="M7 5.5l2 2-1 1.2c.6 1.3 1.6 2.3 2.8 2.8l1.2-1 2 2-1.2 1.5C9.5 14 6 10.5 5.5 7.2z" fill="#1d1d1d"/></svg>
    </li>
    <li>dale@twirlnstep.dance
      <svg class="contact-icon" viewBox="0 0 20 20"><rect x="2" y="5" width="16" height="10.5" fill="#1d1d1d"/><path d="M2.5 5.5L10 11l7.5-5.5" fill="none" stroke="#fff" stroke-width="1.3"/></svg>
    </li>
    <li>www.twirlnstep.com
      <svg class="contact-icon" viewBox="0 0 20 20"><g fill="none" stroke="#1d1d1d" stroke-width="1.4"><circle cx="10" cy="10" r="8"/><ellipse cx="10" cy="10" rx="3.5" ry="8"/><path d="M2 10h16M3.5 6h13M3.5 14h13"/></g></svg>
    </li>
  </ul>
</section>

<section class="card card-back" aria-label="Tagline side">
  <div class="brand">
    <div class="brand-dot"></div>
    <div class="brand-name"><span class="brand-line-top">Twirl N Step</span><span class="brand-line-bottom">Dance</span></div>
  </div>

  <div class="tagline-band">
    <p class="tagline">Yes I would love to Dance</p>
  </div>
  <p class="categories">Social • Exhibition • Competition</p>
</section>

</body>
</html>
```